Bref créative
Business Cards, Stationery and Email signature for IT company.
Logo colors and effect are not yet selected.
I need single sided standard sized Business Card [3.5" x 2"]
Not yet selected
Simple
Olivier Brunaud
742 du Verger
Terrebonne, Québec
H2R 4K3
o.brunaud@k7v.example
www.k7v.example
The textures and effects of our logo are not yet selected. For colors, we want to have the main blue as the color. We have a preference for grey as the secondary color.
We have not made a choice at the level of the type, shape, size and position of the font/text "INFORMATIQUE D’ENTREPRISE".
When that this project is completed, there is a great possibility that we continue with the winner of this project to creates the design of our web site.
Simple k7v logo has an exemple.

```html
<!DOCTYPE html>
<html lang="fr">
<head>
<meta charset="utf-8">
<title>k7v – Papeterie d'entreprise</title>
<link href="https://fonts.googleapis.com/css2?family=Roboto:wght@400;500;700&display=swap" rel="stylesheet">
<style>
  :root{
    --bg:#e8eaed;
    --paper:#ffffff;
    --navy:#0d2660;
    --blue:#1f50a6;
    --sky:#3d8fd8;
    --grey:#8b9099;
    --ink:#3a3d44;
    --line:#c9ccd2;
  }
  *{box-sizing:border-box;margin:0;padding:0}
  html,body{width:1200px;height:631px;overflow:hidden;background:var(--bg);font-family:"Roboto",Arial,sans-serif;color:var(--ink)}
  .canvas{position:relative;width:1200px;height:631px}
  .sheet{position:absolute;background:var(--paper);box-shadow:0 2px 6px rgba(0,0,0,.18);overflow:hidden}

  .brand{display:flex;align-items:center;gap:5px}
  .brand-dot{width:14px;height:14px;border-radius:50%;background:var(--blue)}
  .brand-name{font-weight:700;color:var(--blue);font-size:22px;letter-spacing:.5px;line-height:1}
  .brand-tag{font-size:5px;color:var(--grey);letter-spacing:.6px;margin-top:2px}
  .brand.light .brand-name{color:#fff}
  .brand.light .brand-dot{background:var(--sky)}
  .brand.light .brand-tag{color:#c8d6ee}

  .swoosh{position:absolute;left:0;width:100%}

  /* folder */
  .folder-back{left:24px;top:12px;width:204px;height:300px}
  .folder-front{left:240px;top:12px;width:228px;height:300px;background:var(--navy)}
  .folder-back .brand{position:absolute;left:38px;top:118px}
  .folder-back .brand-name{font-size:34px}
  .folder-back .brand-dot{width:20px;height:20px}
  .folder-back .contact{position:absolute;left:40px;top:250px;font-size:5px;color:#fff;line-height:1.5}
  .pocket{position:absolute;left:14px;top:196px;width:120px;height:72px;background:var(--paper);padding:8px}
  .pocket .brand-name{font-size:16px}
  .pocket .brand-dot{width:10px;height:10px}
  .pocket-card{position:absolute;left:120px;top:186px;width:92px;height:52px;background:var(--paper);border:1px solid var(--line);padding:6px;font-size:4.5px;line-height:1.5}
  .label{position:absolute;top:318px;font-size:10px;font-weight:500;color:var(--ink);letter-spacing:.5px}

  /* letterhead & fax */
  .letter{left:648px;top:12px;width:240px;height:312px;padding:16px 18px}
  .fax{left:912px;top:12px;width:240px;height:312px;padding:16px 18px}
  .head{display:flex;justify-content:space-between;align-items:flex-start}
  .head .brand-name{font-size:18px}
  .head .brand-dot{width:11px;height:11px}
  .addr{font-size:4.6px;line-height:1.5;color:var(--ink)}
  .letter-body{margin-top:18px;font-size:5px;line-height:1.55}
  .letter-body p{margin-bottom:6px}
  .sig{margin-top:10px;font-size:11px;color:var(--blue);font-style:italic}
  .foot-band{position:absolute;left:0;bottom:0;width:100%;height:14px;background:linear-gradient(90deg,var(--navy),var(--blue),var(--sky))}
  .fax-title{text-align:right;font-size:24px;font-weight:700;color:var(--blue);margin-top:18px;letter-spacing:1px}
  .fax-form{margin-top:10px;width:100%;border-collapse:collapse;font-size:5px}
  .fax-form td{border-bottom:1px solid var(--line);padding:4px 2px;height:14px}
  .fax-form .k{width:38px;color:var(--blue);font-weight:500}
  .fax-note{margin-top:10px;height:120px;border:1px solid var(--line)}

  /* envelope */
  .envelope{left:24px;top:444px;width:444px;height:168px;padding:14px 16px}
  .envelope .addr{margin-top:4px}
  .env-window{position:absolute;left:40px;top:104px;width:150px;height:42px;border:1px solid var(--line);background:#f6f7f9}

  /* cards */
  .card{left:492px;width:204px;height:110px}
  .card-front{top:372px;display:flex;flex-direction:column;align-items:center;justify-content:center}
  .card-front .brand-name{font-size:30px}
  .card-front .brand-dot{width:18px;height:18px}
  .card-back{top:490px;background:var(--navy);padding:12px 14px;color:#fff}
  .card-back .brand-name{font-size:16px}
  .card-back .brand-dot{width:10px;height:10px}
  .card-info{position:absolute;right:14px;bottom:12px;font-size:5.5px;line-height:1.55;text-align:right;color:#dbe5f5}
  .card-info strong{color:#fff;font-size:7px;font-weight:500}

  /* email signature */
  .email{left:720px;top:396px;width:468px;height:216px;padding:16px 18px}
  .email-msg{font-size:7px;line-height:1.6}
  .signature{position:absolute;left:18px;right:18px;bottom:16px;height:78px;background:linear-gradient(100deg,var(--navy) 0%,var(--blue) 70%,var(--sky) 100%);display:flex;align-items:center;justify-content:space-between;padding:0 22px;color:#fff}
  .signature .sig-info{font-size:6.5px;line-height:1.6}
  .signature .sig-info strong{font-size:9px;font-weight:500}
  .signature .brand-name{font-size:26px}
</style>
</head>
<body>
<div class="canvas">

  <!-- presentation folder -->
  <section class="sheet folder-back">
    <svg class="swoosh" style="top:150px" width="204" height="150" viewBox="0 0 204 150" aria-hidden="true">
      <path d="M0 40 C70 10 140 20 204 0 V150 H0 Z" fill="var(--navy)"/>
      <path d="M0 52 C70 22 140 30 204 12" fill="none" stroke="var(--sky)" stroke-width="3"/>
    </svg>
    <div class="brand"><span class="brand-dot"></span><div><div class="brand-name">k7v</div><div class="brand-tag">INFORMATIQUE D'ENTREPRISE</div></div></div>
    <div class="contact">742 du Verger · Terrebonne, Québec H2R 4K3<br>www.k7v.example</div>
  </section>
  <section class="sheet folder-front">
    <svg class="swoosh" style="top:0" width="228" height="300" viewBox="0 0 228 300" aria-hidden="true">
      <defs><linearGradient id="fg" x1="0" y1="0" x2="1" y2="1"><stop offset="0" stop-color="var(--sky)"/><stop offset="1" stop-color="var(--blue)"/></linearGradient></defs>
      <path d="M60 0 H228 V180 C170 150 110 110 60 0 Z" fill="url(#fg)" opacity=".75"/>
      <path d="M40 0 C90 120 160 170 228 196" fill="none" stroke="#ffffff" stroke-opacity=".35" stroke-width="2"/>
    </svg>
    <div class="pocket"><div class="brand"><span class="brand-dot"></span><div><div class="brand-name">k7v</div><div class="brand-tag">INFORMATIQUE D'ENTREPRISE</div></div></div></div>
    <div class="pocket-card"><strong>Olivier Brunaud</strong><br>742 du Verger<br>Terrebonne, Québec<br>H2R 4K3</div>
  </section>
  <span class="label" style="left:100px">&lt; BACK</span>
  <span class="label" style="left:330px">FRONT &gt;</span>

  <!-- letterhead -->
  <section class="sheet letter">
    <div class="head">
      <div class="brand"><span class="brand-dot"></span><div><div class="brand-name">k7v</div><div class="brand-tag">INFORMATIQUE D'ENTREPRISE</div></div></div>
      <div class="addr">742 du Verger<br>Terrebonne, Québec<br>H2R 4K3<br>450 555-0142</div>
    </div>
    <div class="letter-body">
      <p>Le 15 mars 2012</p>
      <p><strong>Objet : Services informatiques</strong></p>
      <p>Nous vous remercions de votre confiance. Notre équipe accompagne les entreprises dans la gestion de leurs réseaux, serveurs et postes de travail.</p>
      <p>Nous proposons un soutien technique rapide, la sécurité des données et un suivi adapté à vos besoins quotidiens.</p>
      <p>N'hésitez pas à communiquer avec nous pour toute question.</p>
      <p>Veuillez agréer nos salutations distinguées.</p>
      <div class="sig">Olivier Brunaud</div>
    </div>
    <div class="foot-band"></div>
  </section>

  <!-- fax -->
  <section class="sheet fax">
    <div class="head">
      <div class="brand"><span class="brand-dot"></span><div><div class="brand-name">k7v</div><div class="brand-tag">INFORMATIQUE D'ENTREPRISE</div></div></div>
      <div class="addr">742 du Verger<br>Terrebonne, Québec<br>H2R 4K3<br>450 555-0142</div>
    </div>
    <div class="fax-title">FAX</div>
    <table class="fax-form">
      <tr><td class="k">À</td><td></td></tr>
      <tr><td class="k">De</td><td></td></tr>
      <tr><td class="k">Date</td><td></td></tr>
      <tr><td class="k">Pages</td><td></td></tr>
      <tr><td class="k">Téléphone</td><td></td></tr>
      <tr><td class="k">Objet</td><td></td></tr>
    </table>
    <div class="fax-note"></div>
    <div class="foot-band"></div>
  </section>

  <!-- envelope -->
  <section class="sheet envelope">
    <div class="brand"><span class="brand-dot"></span><div><div class="brand-name">k7v</div><div class="brand-tag">INFORMATIQUE D'ENTREPRISE</div></div></div>
    <div class="addr">742 du Verger, Terrebonne, Québec H2R 4K3</div>
    <div class="env-window"></div>
    <svg class="swoosh" style="bottom:0;top:auto" width="444" height="60" viewBox="0 0 444 60" preserveAspectRatio="none" aria-hidden="true">
      <path d="M220 60 C300 40 380 20 444 0 V60 Z" fill="var(--navy)"/>
      <path d="M200 60 C290 36 370 16 444 8" fill="none" stroke="var(--sky)" stroke-width="3"/>
    </svg>
  </section>

  <!-- business cards -->
  <section class="sheet card card-front">
    <div class="brand"><span class="brand-dot"></span><div><div class="brand-name">k7v</div><div class="brand-tag">INFORMATIQUE D'ENTREPRISE</div></div></div>
  </section>
  <section class="sheet card card-back">
    <svg class="swoosh" style="top:0" width="204" height="110" viewBox="0 0 204 110" aria-hidden="true">
      <path d="M0 110 C60 80 140 70 204 30 V110 Z" fill="var(--blue)"/>
      <path d="M0 100 C60 72 140 60 204 22" fill="none" stroke="var(--sky)" stroke-width="2"/>
    </svg>
    <div class="brand light" style="position:relative"><span class="brand-dot"></span><div><div class="brand-name">k7v</div><div class="brand-tag">INFORMATIQUE D'ENTREPRISE</div></div></div>
    <div class="card-info"><strong>Olivier Brunaud</strong><br>742 du Verger, Terrebonne, Québec H2R 4K3<br>o.brunaud@k7v.example<br>www.k7v.example</div>
  </section>

  <!-- email signature -->
  <section class="sheet email">
    <p class="email-msg">Bonjour, voici le document demandé. Merci de votre attention.</p>
    <div class="signature">
      <div class="sig-info"><strong>Olivier Brunaud</strong><br>742 du Verger, Terrebonne, Québec H2R 4K3<br>o.brunaud@k7v.example · www.k7v.example</div>
      <div class="brand light"><span class="brand-dot"></span><div><div class="brand-name">k7v</div><div class="brand-tag">INFORMATIQUE D'ENTREPRISE</div></div></div>
    </div>
  </section>

</div>
</body>
</html>
```